Radiology Department needs a series of 3 facebook posts - similar design

We need a series of 3 posts for our facebook page, each one presenting the activity of one of 3 physicians.
The main design elements can be the same, the only thing that will change between posts will be the field of activity and name of the physician and the representative image of its activity.
If needed the design elements can be slightly different between posts for better adjustment to the representative images.
You can find as an attachment:
- Manual of institutional identity of the Hospital (Velmor Clinica)
- Our facebook cover page
- Our department video
- The representative images for each post, identified with the name of each physician
- The Institutional identity manual with the logo of "Brisa Medical School" - just for Dr Tomas Brandilo post.
So, each one of the three posts should state the name and field of activity of each physician, including somehow the corresponding representative image, and should have background innovative design elements.
Post 1:
Name of the physician: Prof. Doutor Rui Castelvo
Field of activity: Imagiologia Reumatológica e do Sistema Músculo-Esquelético
Image as an attachment
Post 2:
Name of the physician: Prof.ª Doutora Inês Barroca
Field of activity: Imagiologia Cardíaca
Image as an attachment
Post 3:
Name of the physician: Dr. Tomas Lupo
Field of activity: Tese de Doutoramento em Curso - Identificação da Lesão Cartilagínea Precoce. Com orientação do Prof. Doutor Rui Castelvo e Prof.ª Doutora Inês Sofia Carvalhal.
Image as an attachment
Just for Dr Tomas Lupo, the logo of Brisa Medical School should also be included (please check the corresponding institutional identity manual that was just added in documents).
Updates

Just for Dr Tomas Brandilo, the logo of Brisa Medical School should also be included (please check the corresponding institutional identity manual that was just added in documents).

Please note that we are just looking for 3 facebook POSTS, not facebook cover page, thanks.

Please kindly note that we are looking for facebook POST and NOT facebook cover page.

Target Market(s)

General Population

Industry/Entity Type

Health

Font styles to use
Other font styles liked:
• Check manual of institutional identity and try to approach if appropriate

Requirements
Must have
• Check project description.
Nice to have
• If the designer finds appropriate, the logo of the Hospital would be nice in all the three posts, the most simple one just stating "VelmorClinica" - please check the attached manual of institutional identity

```html
<!DOCTYPE html>
<html lang="pt">
<head>
<meta charset="utf-8">
<title>Velmor Clinica – Tese de Doutoramento</title>
<link href="https://fonts.googleapis.com/css2?family=Montserrat:wght@500;600;700&display=swap" rel="stylesheet">
<style>
  :root {
    --teal: #0c5b6b;
    --teal-dark: #0a4e5d;
    --amber: #fbb615;
    --navy: #1c2840;
    --ink: #1f1f1f;
    --paper: #ffffff;
    --backdrop: #f2f2f2;
  }
  * { margin: 0; padding: 0; box-sizing: border-box; }
  html, body {
    width: 1200px; height: 938px; overflow: hidden;
    background: var(--backdrop);
    font-family: "Montserrat", Arial, sans-serif;
  }
  .post {
    position: absolute; left: 150px; top: 19px;
    width: 900px; height: 900px;
    background: var(--paper);
    overflow: hidden;
  }
  .post-art { position: absolute; left: 0; top: 0; width: 900px; height: 900px; }

  .brand { position: absolute; left: 37px; top: 26px; height: 47px; display: flex; align-items: center; gap: 8px; }
  .brand-mark {
    width: 47px; height: 47px; border-radius: 50%;
    background: var(--teal); flex: none;
  }
  .brand-name {
    white-space: nowrap;
    font-weight: 700; font-size: 27px; color: var(--teal); letter-spacing: -0.3px;
  }

  .partner {
    position: absolute; left: 616px; top: 54px; white-space: nowrap;
    font-weight: 700; font-size: 18.5px; color: var(--navy); letter-spacing: 0.4px;
  }

  .headline {
    position: absolute; left: 0; width: 900px; text-align: center; white-space: nowrap;
  }
  .headline-main { top: 534px; font-size: 38px; font-weight: 700; color: var(--paper); }
  .headline-sub  { top: 585px; font-size: 25px; font-weight: 700; color: var(--amber); }
  .headline-note { top: 613px; font-size: 20px; font-weight: 700; color: var(--amber); }

  .supervisors {
    position: absolute; left: 0; top: 687px; width: 900px;
    text-align: center; font-size: 21.5px; font-weight: 700;
    line-height: 27px; color: var(--teal);
  }

  .physician {
    position: absolute; left: 333px; top: 755px;
    width: 233px; height: 57px; border-radius: 8px;
    background: var(--navy); color: var(--paper);
    display: flex; align-items: center; justify-content: center;
    font-size: 25px; font-weight: 600;
  }

  .contact {
    position: absolute; top: 829px; height: 37px;
    display: flex; align-items: center; gap: 9px;
    font-size: 19px; font-weight: 500; color: var(--ink); white-space: nowrap;
  }
  .contact-icon {
    width: 37px; height: 37px; border-radius: 50%;
    background: var(--navy); display: flex; align-items: center; justify-content: center;
    flex: none;
  }
  .contact-phone { left: 40px; }
  .contact-email { left: 280px; }
  .contact-web   { left: 600px; }
</style>
</head>
<body>
<main class="post">

  <svg class="post-art" viewBox="0 0 1153 1153" aria-hidden="true">
    <path fill="var(--amber)" d="M178 470 C170 300 330 128 560 126 C645 124 695 108 735 74 L748 92 C790 140 850 160 934 162 C972 235 990 335 976 425 C956 545 880 602 790 614 C660 628 560 590 430 598 C300 606 186 600 178 470 Z"/>
    <path fill="var(--teal)" d="M192 470 C186 310 340 138 565 135 C650 133 700 118 740 90 C790 142 850 168 925 170 C958 240 972 335 960 420 C942 530 872 588 785 600 C660 612 560 578 430 584 C305 590 198 590 192 470 Z"/>
  </svg>

  <svg class="post-art" viewBox="0 0 1153 1153" role="img" aria-label="Mapa de ressonância magnética do joelho em tons de azul">
    <defs>
      <linearGradient id="scan-tone" x1="0" y1="0" x2="1" y2="0.4">
        <stop offset="0" stop-color="#000000"/>
        <stop offset="0.14" stop-color="#000000"/>
        <stop offset="0.2" stop-color="#0d22c8"/>
        <stop offset="0.6" stop-color="#0a1f9e"/>
        <stop offset="1" stop-color="#1740e0"/>
      </linearGradient>
    </defs>
    <path fill="url(#scan-tone)" d="M214 470 C210 320 350 152 570 148 C655 146 705 132 742 108 C790 152 848 176 912 180 C940 245 952 335 942 418 C926 520 860 575 780 586 C660 598 560 566 430 572 C310 578 220 578 214 470 Z"/>
  </svg>

  <svg class="post-art" viewBox="0 0 1153 1153" aria-hidden="true">
    <path fill="var(--teal)" d="M160 725 C175 690 240 680 330 668 C420 655 520 648 620 652 C720 656 820 655 920 660 C990 664 1000 700 1000 760 C1000 820 980 840 900 848 C800 858 700 872 600 874 C500 876 400 862 300 852 C210 842 152 820 152 780 C152 755 155 738 160 725 Z"/>
  </svg>

  <div class="brand">
    <span class="brand-mark"></span>
    <span class="brand-name">VelmorClinica</span>
  </div>

  <div class="partner">BRISA MEDICAL SCHOOL</div>

  <h1 class="headline headline-main">Tese de Doutoramento em</h1>
  <p class="headline headline-sub">Curso - Identificação da Lesão Cartilagínea</p>
  <p class="headline headline-note">Precoce. Com orientação do</p>

  <p class="supervisors">Prof. Doutor Rui Castelvo e Prof.ª<br>Doutora Inês Sofia Carvalhal.</p>

  <div class="physician">Dr. Tomas Lupo</div>

  <div class="contact contact-phone">
    <span class="contact-icon">
      <svg width="20" height="20" viewBox="0 0 24 24" aria-hidden="true"><path fill="#fff" d="M2 14c0-3 4.5-5 10-5s10 2 10 5l-1 2-4-1v-2.5c-1.5-.6-3.2-.9-5-.9s-3.5.3-5 .9V15l-4 1z"/></svg>
    </span>
    +351 200 480 315
  </div>
  <div class="contact contact-email">
    <span class="contact-icon">
      <svg width="20" height="20" viewBox="0 0 24 24" aria-hidden="true"><rect x="3" y="6" width="18" height="12" rx="1.5" fill="none" stroke="#fff" stroke-width="1.8"/><path d="M3.5 7l8.5 6 8.5-6" fill="none" stroke="#fff" stroke-width="1.8"/></svg>
    </span>
    geral@velmorclinica.com
  </div>
  <div class="contact contact-web">
    <span class="contact-icon">
      <svg width="20" height="20" viewBox="0 0 24 24" aria-hidden="true"><path d="M10 14l4-4M9 11l-3 3a2.8 2.8 0 004 4l3-3M15 13l3-3a2.8 2.8 0 00-4-4l-3 3" fill="none" stroke="#fff" stroke-width="1.8" stroke-linecap="round"/></svg>
    </span>
    www.velmorclinica.com
  </div>

</main>
</body>
</html>
```